Engineering group involved with fire safety needs a business card

We need a business card design for a company based in Greece called "Varotis Group". We are engineers and specialized technicians, operating the following : a) Fire fighting equipment trade b) Installation , Inspection & Maintenance of fire extinguishers and fire protection systems c) Occupational Health & Safety (Risk assessment & management/ Staff training). We need a clear and simple card design. I uploaded a draft I made, in order to give you an idea of the company and how I currently imagine the design of the card. I also uploaded the logo in .png file format. We are always open to different, new suggestions and ideas you may want to submit.
Target Market(s)
industries, companies, managers, retail clients
Industry/Entity Type
Fire Safety
Contact Information for Business Card
Addresses & phone numbers (headquarters + branch), logo, name (you can find all the details on the uploaded files!)
Colors
Designer to choose colors to be used in the design.
Look and feel
Each slider illustrates characteristics of the customer's brand and the style your logo design should communicate.

```html
<!DOCTYPE html>
<html lang="en">
<head>
<meta charset="utf-8">
<title>Varotis Group — Business Card</title>
<link href="https://fonts.googleapis.com/css2?family=Montserrat:wght@300;400;500;700&display=swap" rel="stylesheet">
<style>
  :root {
    --red: #b3232a;
    --grey: #5f6466;
    --ink: #1c1c1c;
    --paper: #ffffff;
    --dark: #212121;
    --light-text: #e6e6e6;
    --stage: #d9d9d9;
  }
  * { margin: 0; padding: 0; box-sizing: border-box; }
  html, body { width: 1200px; height: 900px; overflow: hidden; }
  body {
    background: var(--stage);
    font-family: "Montserrat", sans-serif;
    position: relative;
  }
  .card {
    position: absolute;
    top: 65px;
    width: 440px;
    height: 770px;
    padding: 60px 48px;
    box-shadow: 0 6px 18px rgba(0,0,0,0.18);
  }
  .card--front { left: 120px; background: var(--paper); color: var(--ink); }
  .card--back { left: 640px; background: var(--dark); color: var(--light-text); text-align: center; }

  .brand { display: flex; align-items: center; gap: 14px; }
  .card--back .brand { justify-content: center; margin-top: 40px; }
  .brand__mark { width: 34px; height: 34px; background: var(--grey); flex: none; }
  .card--back .brand__mark { background: var(--red); }
  .brand__name {
    font-weight: 700;
    font-size: 34px;
    letter-spacing: 1px;
    color: var(--red);
    line-height: 1;
  }
  .card--back .brand__name { color: var(--paper); }
  .tagline {
    font-weight: 300;
    font-size: 14.5px;
    color: var(--ink);
    margin-top: 14px;
    padding-top: 10px;
    border-top: 2px solid var(--grey);
    display: inline-block;
  }
  .card--back .tagline { color: var(--light-text); border-top-color: var(--light-text); }

  .person { margin-top: 46px; }
  .person__name { font-weight: 700; font-size: 27px; letter-spacing: 0.3px; }
  .person__role { color: var(--red); font-weight: 500; font-size: 20px; line-height: 1.2; margin-top: 6px; }
  .divider { width: 30px; height: 4px; background: var(--ink); margin: 30px 0 40px; }

  .contact { font-size: 17px; font-weight: 400; line-height: 1.55; }
  .contact .label { color: var(--red); font-weight: 500; }
  .contact .gap { margin-top: 10px; }
  .contact .web { margin-top: 14px; }
  .contact .web span { color: var(--red); }

  .services {
    margin-top: 110px;
    font-size: 17px;
    font-weight: 400;
    line-height: 1.75;
  }
  .services p + p { margin-top: 10px; }
  .links { margin-top: 110px; font-size: 16px; font-weight: 300; line-height: 1.8; }
</style>
</head>
<body>
  <section class="card card--front">
    <div class="brand">
      <span class="brand__mark"></span>
      <span class="brand__name">VAROTIS GROUP</span>
    </div>
    <span class="tagline">Installation-Inspection-Maintenance</span>

    <div class="person">
      <h1 class="person__name">STAVROS KALAMARIS</h1>
      <p class="person__role">Mechanical Engineer-<br>OHS Consultant</p>
    </div>
    <div class="divider"></div>

    <div class="contact">
      <p><span class="label">Tel.</span> (HQ) +30 22810 45302</p>
      <p><span class="label">Tel.</span> (BQ) +30 210 5517429</p>
      <p><span class="label">Mob.</span> +30 694 215 73 08</p>
      <p>stavros.kalamaris@varotisgroup.gr</p>
      <p class="gap label">Headquarters:</p>
      <p>14 Anemonis, 19400 Koropi</p>
      <p class="label">Branch Office:</p>
      <p>22 Thalassis, 15231 Chalandri</p>
      <p class="web">www.<span>varotisgroup.gr</span></p>
    </div>
  </section>

  <section class="card card--back">
    <div class="brand">
      <span class="brand__mark"></span>
      <span class="brand__name">VAROTIS GROUP</span>
    </div>
    <span class="tagline">Installation-Inspection-Maintenance</span>

    <div class="services">
      <p>Fire fighting equipment trade</p>
      <p>Installation , Inspection &amp; Maintenance<br>of fire extinguishers and fire<br>protection systems</p>
      <p>Occupational Health &amp; Safety</p>
    </div>

    <div class="links">
      <p>www.varotisgroup.gr</p>
      <p>info@varotisgroup.gr</p>
    </div>
  </section>
</body>
</html>
```